Store Front / Boutique Front window signage

I am looking to have a sign printed to stick on the glass of my new Kitchens Cabinets showroom. I already have a logo that I will include however this is the "Boutique" location so I am looking to have my logo incorporated for brand recognition but I do not want just my logo. I want something classy, minimalist with class. Maybe even old school or vintage in style. I will include my store front window sizes and a picture of the store front.

My thought is to take my logo small to moderate in size. Take away the "Cabinetry and Design" part and place that statement larger like this
"Cabinetry and Design Boutique"
My website is Brambleworthkitchens.com
window panes are as follows
left is 72 3/4" wide
right is 70" wide
height is 97 1/2"

I would like to see something not too large , across the two panes
Updates

I have been with work family , looking to choose the best created design and then modify to my liking

Target Market(s)

People !

Font styles to use
Decorative
Script
Other font styles liked:
• vintage , classic

Requirements
Must have
• Tasteful . Maybe logo and small strip along the bottom with a manufacturers logos.
Should not have
• Should not be too large, the signage is not intended to be seen from driving by , more for foot traffic

```html
<!DOCTYPE html>
<html lang="en">
<head>
<meta charset="utf-8">
<title>Brambleworth Kitchens — Cabinetry &amp; Design Boutique</title>
<link rel="stylesheet" href="https://fonts.googleapis.com/css2?family=Marcellus&display=swap">
<style>
  :root {
    --glass: #2a2420;
    --ink: #ffffff;
    --rule: #f4f1ec;
    --shade: rgba(0, 0, 0, 0.5);
  }
  html, body {
    margin: 0;
    padding: 0;
    width: 1200px;
    height: 1006px;
    overflow: hidden;
    background: var(--glass);
  }
  .window-sign {
    position: absolute;
    left: 140px;
    top: 250px;
    width: 920px;
    color: var(--ink);
    font-family: "Marcellus", serif;
  }
  .brand-row {
    display: flex;
    align-items: flex-end;
    gap: 18px;
    height: 70px;
  }
  .brand-row .rule {
    flex: 1;
    height: 2px;
    background: var(--rule);
    margin-bottom: 4px;
  }
  .brand-name {
    font-weight: 400;
    font-size: 30px;
    line-height: 1;
    letter-spacing: 2px;
    text-transform: uppercase;
    white-space: nowrap;
  }
  .headline {
    margin: 0;
    font-weight: 400;
  }
  .headline-line {
    display: block;
    text-align: center;
    font-size: 100px;
    line-height: 138px;
    height: 138px;
    letter-spacing: 12px;
    padding-left: 12px;
    text-transform: uppercase;
    border-bottom: 2px solid var(--rule);
    text-shadow: 3px 3px 0 var(--shade);
    white-space: nowrap;
    overflow: hidden;
  }
</style>
</head>
<body>
  <main class="window-sign">
    <div class="brand-row">
      <span class="rule"></span>
      <span class="brand-name">Brambleworth Kitchens</span>
    </div>
    <h1 class="headline">
      <span class="headline-line">Cabinetry</span>
      <span class="headline-line">&amp; Design</span>
      <span class="headline-line">Boutique</span>
    </h1>
  </main>
</body>
</html>
```